Flyer Design for mobile emergency tool and vehicle up-fitting services company

trifold flyer design for a uplifting company that does poly - plastic manufacturing for FIRE, EMS and POLICE vehicles. We design and manufacture poly systems for tools, custom storage solutions. We install vehicle lifts, lights, sirens, consoles, cabinets etc. We use CNC to design custom mounting projects for first responders

Target Market(s)

FIRE, EMS, MILITARY and POLICE

Industry/Entity Type

emergency services

Font styles to use
Serif

Colors
EB3D1F
EC4F4E
F09395
F8D3D4
FCEDEE

Requirements
Must have
• multiple pictures
Nice to have
• background design that is related to my current market

```html
<!DOCTYPE html>
<html lang="en">
<head>
<meta charset="utf-8">
<title>Rescueline Works – Trifold Flyer</title>
<link href="https://fonts.googleapis.com/css2?family=Poppins:wght@400;500;600;700&family=Oswald:wght@400;500;600&family=Rokkitt:wght@800;900&display=swap" rel="stylesheet">
<style>
:root{
  --red:#d2141d;
  --red-deep:#8e0a0e;
  --red-soft:#ec4f4e;
  --pink:#f8d3d4;
  --blush:#fcedee;
  --ink:#1b1b1f;
  --panel-dark:#1f1f24;
  --black:#0c0c0d;
  --navy:#1d2a6b;
  --paper:#ffffff;
  --rule:#8a8a8a;
}
*{box-sizing:border-box;margin:0;padding:0}
html,body{width:1200px;height:2400px;overflow:hidden;background:#f4f4f5}
body{font-family:"Poppins",sans-serif;color:var(--ink);position:relative}
.spread{position:absolute;left:50px;width:1100px;height:778px;display:grid;grid-template-columns:repeat(3,1fr);box-shadow:0 12px 40px rgba(0,0,0,.22);background:var(--paper)}
.spread--outside{top:360px}
.spread--inside{top:1290px}
.panel{position:relative;overflow:hidden}
.panel--light{background:var(--paper)}
.panel--dark{background:var(--panel-dark);color:#fff}
.panel--black{background:var(--black)}
.abs{position:absolute}
.photo{position:absolute}
.photo--engine{background:linear-gradient(135deg,#8e1218,#c62a2e 45%,#5a5f66)}
.photo--tools{background:linear-gradient(160deg,#3b3d42,#7b7f86 50%,#2a2b2e)}
.photo--yellow{background:linear-gradient(150deg,#d9c25a,#8a8b8f 55%,#3c3e42)}
.photo--drawer{background:linear-gradient(140deg,#b8241f,#d9c25a 50%,#9a9da2)}
.photo--crew{background:linear-gradient(170deg,#2b2c31,#494b50 45%,#c9cacd)}
.photo--sky{background:linear-gradient(180deg,#3b74c4,#7fa8dc 45%,#b9242a 75%,#2b2b2b)}
.framed{border:5px solid #fff}

.tab{position:absolute;left:0;top:33px;width:240px;height:36px}
.tab span{position:absolute;left:32px;top:3px;font:700 22px/30px "Poppins",sans-serif;color:#fff;letter-spacing:.3px}
.icon-tile{position:absolute;left:50%;transform:translateX(-50%);width:56px;height:56px;background:var(--red);display:flex;align-items:center;justify-content:center}
.service-text{position:absolute;left:20px;right:20px;text-align:center;font:500 15.5px/19px "Poppins",sans-serif}
.divider{position:absolute;left:30px;right:30px;height:1px;background:var(--rule)}

.hours{position:absolute;left:28px;top:79px;display:flex;align-items:flex-start}
.hours__num{font:500 92px/76px "Oswald",sans-serif;color:#fff;letter-spacing:-3px;position:relative;padding-right:4px}
.hours__unit{position:absolute;left:38px;bottom:4px;background:var(--panel-dark);font:500 12px/13px "Poppins",sans-serif;letter-spacing:0;padding:0 2px;white-space:nowrap}
.hours__label{margin-left:10px;margin-top:4px;font:500 31px/32px "Poppins",sans-serif;letter-spacing:.5px;background:linear-gradient(90deg,var(--red),var(--red-deep));padding:0 6px;white-space:nowrap}
.sector{position:absolute;display:flex;align-items:center;gap:10px;font:600 19px "Poppins",sans-serif}
.sector__tile{width:52px;height:52px;background:#fff;border-radius:4px;display:flex;align-items:center;justify-content:center}
.contact{position:absolute;left:0;right:0;text-align:center;font:400 13px/17px "Poppins",sans-serif;color:#fff}
.contact__dots{display:block;width:22px;margin:2px auto;border-top:1px dotted #aaa}
.url-plain{font-weight:600}

.brand{position:absolute;left:0;right:0;top:38px;text-align:center}
.brand__mark{width:70px;height:70px;border-radius:50%;border:3px solid var(--ink);margin:0 auto}
.brand__name{margin-top:8px;font:700 16px/18px "Poppins",sans-serif;color:var(--ink);letter-spacing:1px}

.title-serif{position:absolute;left:0;right:0;top:578px;text-align:center;font:900 34px/36px "Rokkitt",serif;color:var(--ink)}
.title-serif em{font-style:normal;color:var(--red)}
.title-sub{position:absolute;left:0;right:0;top:613px;text-align:center;font:500 26px/28px "Poppins",sans-serif;color:var(--ink)}
.title-sectors{position:absolute;left:50%;top:640px;white-space:nowrap;font:500 29px/32px "Oswald",sans-serif;color:var(--navy);transform:translateX(-50%) scaleX(.92)}
.tagline{position:absolute;left:0;right:0;top:680px;text-align:center;font:500 13.5px/16px "Poppins",sans-serif}
.url-pill{position:absolute;left:44px;right:44px;top:713px;height:30px;border-radius:4px;background:var(--red);color:#fff;text-align:center;font:600 16px/30px "Poppins",sans-serif}

.red-head{position:absolute;left:50%;white-space:nowrap;font:500 21px/26px "Oswald",sans-serif;color:var(--red);transform:translateX(-50%) scaleX(.88)}
.body-text{position:absolute;left:26px;right:26px;text-align:center;font:400 14.5px/17px "Poppins",sans-serif}
.point{position:absolute;left:38px;right:20px;display:flex;align-items:center;gap:16px;font:500 15.5px/19px "Poppins",sans-serif}
.point__tile{flex:0 0 46px;height:52px;background:linear-gradient(180deg,var(--red),var(--red-deep));display:flex;align-items:center;justify-content:center}
svg{display:block}
</style>
</head>
<body>

<section class="spread spread--outside">

  <article class="panel panel--light">
    <svg class="tab" viewBox="0 0 240 36" aria-hidden="true">
      <polygon points="0,0 205,0 222,36 0,36" fill="var(--red)"/>
      <polygon points="212,0 220,0 237,36 229,36" fill="var(--red)"/>
    </svg>
    <div class="tab" style="background:none"><span>WHAT WE DO</span></div>

    <div class="icon-tile" style="top:93px">
      <svg width="34" height="34" viewBox="0 0 24 24" fill="none" stroke="#fff" stroke-width="2"><circle cx="12" cy="12" r="8"/><path d="M8 16l6-6M13 7l4 4"/></svg>
    </div>
    <p class="service-text" style="top:160px">We design and manufacture poly systems for tools, custom storage solutions.</p>

    <div class="icon-tile" style="top:230px">
      <svg width="34" height="34" viewBox="0 0 24 24" fill="#fff"><path d="M7 20v-8a5 5 0 0 1 10 0v8z"/><rect x="4" y="20" width="16" height="2"/><path d="M12 1v3M4 5l2 2M20 5l-2 2" stroke="#fff" stroke-width="2"/></svg>
    </div>
    <p class="service-text" style="top:303px">We install vehicle lifts, lights, sirens, consoles, cabinets etc.</p>

    <div class="icon-tile" style="top:362px">
      <svg width="34" height="34" viewBox="0 0 24 24" fill="none" stroke="#fff" stroke-width="2"><circle cx="9" cy="14" r="5"/><circle cx="9" cy="14" r="1.5" fill="#fff"/><rect x="14" y="3" width="7" height="7"/></svg>
    </div>
    <p class="service-text" style="top:433px">We use CNC to design custom mounting projects for first responders</p>

    <svg class="abs" style="left:0;top:489px" width="367" height="289" viewBox="0 0 367 289" aria-hidden="true">
      <defs><linearGradient id="redFadeA" x1="0" x2="1"><stop offset="0" stop-color="var(--red-deep)"/><stop offset="1" stop-color="var(--red)"/></linearGradient></defs>
      <polygon points="0,0 180,40 0,80" fill="url(#redFadeA)"/>
      <polygon points="367,0 367,30 190,48" fill="var(--red)"/>
    </svg>
    <div class="photo photo--engine" role="img" aria-label="Fire engine side compartments" style="left:0;top:545px;width:162px;height:233px;clip-path:polygon(0 12%,100% 0,100% 100%,0 100%)"></div>
    <div class="photo photo--tools" role="img" aria-label="Rescue tools stored in a compartment" style="left:176px;top:513px;width:180px;height:134px;clip-path:polygon(0 8%,100% 0,100% 100%,0 100%)"></div>
    <div class="photo photo--drawer" role="img" aria-label="Slide-out tray with hydraulic tools" style="left:176px;top:655px;width:180px;height:123px"></div>
  </article>

  <article class="panel panel--dark">
    <div class="hours">
      <div class="hours__num">24<span class="hours__unit">hours</span></div>
      <div class="hours__label">EMERGENCY<br>SERVICE FOR</div>
    </div>

    <div class="sector" style="left:36px;top:183px">
      <span class="sector__tile"><svg width="30" height="30" viewBox="0 0 24 24" fill="var(--red)"><rect x="7" y="7" width="8" height="15" rx="2"/><rect x="9" y="3" width="4" height="4"/><path d="M13 4h5l2 2" stroke="var(--red)" stroke-width="2" fill="none"/></svg></span>FIRE
    </div>
    <div class="sector" style="left:196px;top:183px">
      <span class="sector__tile"><svg width="32" height="32" viewBox="0 0 24 24" fill="var(--red)"><path d="M1 7h14v11H1zM15 10h4l4 4v4h-8z"/><circle cx="6" cy="19" r="2" fill="#fff" stroke="var(--red)"/><circle cx="18" cy="19" r="2" fill="#fff" stroke="var(--red)"/><path d="M7 9v6M4 12h6" stroke="#fff" stroke-width="2"/></svg></span>EMS
    </div>
    <div class="sector" style="left:36px;top:267px">
      <span class="sector__tile"><svg width="34" height="30" viewBox="0 0 26 22" fill="var(--red)"><rect x="7" y="5" width="10" height="5"/><rect x="17" y="6" width="8" height="2"/><rect x="2" y="10" width="22" height="6" rx="3"/><circle cx="6" cy="18" r="2"/><circle cx="13" cy="18" r="2"/><circle cx="20" cy="18" r="2"/></svg></span>MILITARY
    </div>
    <div class="sector" style="left:196px;top:267px">
      <span class="sector__tile"><svg width="30" height="30" viewBox="0 0 24 24" fill="var(--red)"><path d="M12 2l8 3v6c0 5-3.5 9-8 11-4.5-2-8-6-8-11V5z"/><path d="M12 7l1.5 3 3 .4-2.2 2 .6 3-2.9-1.6-2.9 1.6.6-3-2.2-2 3-.4z" fill="#fff"/></svg></span>POLICE
    </div>

    <div class="photo photo--engine" role="img" aria-label="Engine compartment with storage shelves" style="left:0;top:338px;width:180px;height:180px"></div>
    <div class="photo photo--tools" role="img" aria-label="Open equipment bay" style="left:188px;top:338px;width:179px;height:95px"></div>
    <div class="photo photo--yellow" role="img" aria-label="Yellow tool mounts on a slide tray" style="left:188px;top:440px;width:179px;height:78px"></div>

    <svg class="abs" style="left:109px;top:584px" width="150" height="20" viewBox="0 0 150 20" aria-hidden="true">
      <line x1="10" y1="10" x2="140" y2="10" stroke="#fff" stroke-width="1.5"/>
      <circle cx="10" cy="10" r="9" fill="#fff"/><path d="M6 6c0 5 3 8 8 8l1-2-2-1-1 1c-2-1-3-2-4-4l1-1-1-2z" fill="var(--red)"/>
      <circle cx="75" cy="10" r="9" fill="#fff"/><path d="M75 4a4 4 0 0 1 4 4c0 3-4 7-4 7s-4-4-4-7a4 4 0 0 1 4-4z" fill="var(--red)"/>
      <circle cx="140" cy="10" r="9" fill="#fff"/><rect x="135" y="7" width="10" height="7" fill="var(--red)"/><path d="M135 7l5 4 5-4" stroke="#fff" fill="none"/>
    </svg>
    <div class="contact" style="top:616px">011 555 010 2024<span class="contact__dots"></span></div>
    <div class="contact" style="top:646px">Lorem ipsum city,<br>lorem ipsum state, 75612<span class="contact__dots"></span></div>
    <div class="contact" style="top:692px">info@rescueline.example</div>
    <div class="contact url-plain" style="top:723px">www.rescuelineworks.example</div>
  </article>

  <article class="panel panel--light">
    <div class="brand">
      <div class="brand__mark"></div>
      <div class="brand__name">RESCUELINE WORKS</div>
    </div>
    <svg class="abs" style="left:0;top:130px" width="367" height="420" viewBox="0 0 367 420" aria-hidden="true">
      <defs><linearGradient id="redFadeC" x1="0" x2="1"><stop offset="0" stop-color="var(--red-deep)"/><stop offset="1" stop-color="var(--red)"/></linearGradient></defs>
      <polygon points="0,0 160,40 0,110" fill="url(#redFadeC)"/>
      <polygon points="367,330 367,408 170,408" fill="var(--red)"/>
    </svg>
    <div class="photo photo--engine" role="img" aria-label="Saw and tools on a red engine shelf" style="left:0;top:180px;width:165px;height:126px;clip-path:polygon(0 10%,100% 0,100% 100%,0 100%)"></div>
    <div class="photo photo--tools" role="img" aria-label="Hydraulic rescue tools mounted in a bay" style="left:175px;top:138px;width:192px;height:168px;clip-path:polygon(0 14%,100% 0,100% 100%,0 100%)"></div>
    <div class="photo photo--yellow" role="img" aria-label="Vertical tool racks in a compartment" style="left:0;top:314px;width:165px;height:124px"></div>
    <div class="photo photo--engine" role="img" aria-label="Storage bay with red equipment" style="left:175px;top:314px;width:192px;height:124px"></div>
    <div class="photo photo--tools" role="img" aria-label="Cut-off saw on a mount" style="left:0;top:446px;width:165px;height:92px"></div>
    <div class="photo photo--drawer" role="img" aria-label="Generator and fan in a compartment" style="left:175px;top:446px;width:192px;height:92px;clip-path:polygon(0 0,100% 0,100% 70%,0 100%)"></div>

    <h1 class="title-serif"><em>POLY</em> - PLASTIC</h1>
    <p class="title-sub">MANUFACTURER FOR</p>
    <p class="title-sectors">FIRE, EMS AND POLICE VEHICLES</p>
    <p class="tagline">Mobile Emergency Tool And Vehicle<br>Up-Fitting Services Company</p>
    <div class="url-pill">www.rescuelineworks.example</div>
  </article>
</section>

<section class="spread spread--inside">

  <article class="panel panel--light">
    <div class="icon-tile" style="top:54px">
      <svg width="30" height="30" viewBox="0 0 24 24"><path d="M12 2l8 3v6c0 5-3.5 9-8 11-4.5-2-8-6-8-11V5z" fill="#fff"/><path d="M8 12l3 3 5-6" stroke="var(--red)" stroke-width="2.4" fill="none"/></svg>
    </div>
    <p class="service-text" style="top:123px">Rescueline Apparatus understands the importance of keeping your first out tools safe, secure, and easily accessible.</p>
    <div class="divider" style="top:214px"></div>
    <div class="icon-tile" style="top:247px">
      <svg width="30" height="30" viewBox="0 0 24 24"><rect x="4" y="4" width="16" height="18" rx="2" fill="#fff"/><rect x="9" y="2" width="6" height="4" fill="#fff" stroke="var(--red)"/><path d="M8 13l3 3 5-6" stroke="var(--red)" stroke-width="2.4" fill="none"/></svg>
    </div>
    <p class="service-text" style="top:324px">The task of organizing and securing your equipment while utilizing all of your compartment space can be complicated.</p>

    <div class="photo photo--engine" role="img" aria-label="Firefighter with extinguisher beside an open engine compartment" style="left:0;top:418px;width:367px;height:360px;clip-path:polygon(0 22%,100% 0,100% 100%,0 100%)"></div>
    <svg class="abs" style="left:0;top:418px" width="367" height="120" viewBox="0 0 367 120" aria-hidden="true">
      <defs><linearGradient id="redFadeD" x1="1" x2="0"><stop offset="0" stop-color="var(--red-deep)"/><stop offset="1" stop-color="var(--red)"/></linearGradient></defs>
      <polygon points="367,0 367,90 175,60" fill="url(#redFadeD)"/>
    </svg>
  </article>

  <article class="panel panel--black">
    <div class="photo photo--yellow framed" role="img" aria-label="Yellow poly tool holders on a slide tray" style="left:30px;top:38px;width:309px;height:120px"></div>
    <div class="photo photo--crew framed" role="img" aria-label="Firefighter in red helmet at a vehicle" style="left:30px;top:176px;width:154px;height:278px"></div>
    <div class="photo photo--tools framed" role="img" aria-label="Hose reels in a compartment" style="left:198px;top:176px;width:141px;height:130px"></div>
    <div class="photo photo--engine framed" role="img" aria-label="Fire engine parked in snow" style="left:198px;top:314px;width:141px;height:140px"></div>
    <div class="photo photo--drawer framed" role="img" aria-label="Red tools on a pull-out tray" style="left:30px;top:470px;width:309px;height:137px"></div>
    <div class="photo photo--sky framed" role="img" aria-label="Open vehicle compartment under blue sky" style="left:30px;top:625px;width:309px;height:124px"></div>
  </article>

  <article class="panel panel--light">
    <div class="photo photo--crew" role="img" aria-label="Firefighter in turnout gear walking through smoke beside an engine" style="left:0;top:0;width:367px;height:292px;background:linear-gradient(150deg,#a1161b,#3a3b40 45%,#c9cbcf)"></div>
    <h2 class="red-head" style="top:322px">RESCUELINE IS OWNED AND OPERATED</h2>
    <p class="body-text" style="top:360px">by first responders and tour company is dedicated to the brothers and sisters that are on the frontline every day.</p>
    <h2 class="red-head" style="top:427px">STOP PUTTING YOUR EMERGENCY VEHICLES</h2>
    <p class="body-text" style="top:463px">out of service, we will come to you!&nbsp; We have a mobile fabrication unit that will come onsite for custom installs</p>
    <div class="point" style="top:540px">
      <span class="point__tile"><svg width="28" height="28" viewBox="0 0 24 24" fill="none" stroke="#fff" stroke-width="2"><path d="M9 18h6M10 21h4M12 3a6 6 0 0 0-4 10.5V16h8v-2.5A6 6 0 0 0 12 3z"/></svg></span>
      <span>It is our duty is to produce innovative tool-specific</span>
    </div>
    <div class="divider" style="top:626px"></div>
    <div class="point" style="top:656px">
      <span class="point__tile"><svg width="28" height="28" viewBox="0 0 24 24" fill="#fff"><rect x="2" y="10" width="4" height="11"/><path d="M8 10l4-7c1.5 0 2 1 1.7 2.5L13 9h7c1 0 2 1 1.7 2l-2 8c-.3 1-1 2-2 2H8z"/></svg></span>
      <span>Rescueline makes it easy with a line of products custom built for your needs.</span>
    </div>
  </article>
</section>

</body>
</html>
```